Brennick Holdings Business Cards

These are professional business cards that are for my family office.
Put fake emails and phone numbers as of now until I finalize those components. This family office controls my families investments, assets, and future. The cards should be professional.
..
.
.
.
I just uploaded another variation of a logo I would like to see as a business card to I am inbeteen which logo to use

Target Market(s)

business

Industry/Entity Type

business

Contact Information for Business Card

Professional, wealth related, finance related.

Requirements
Must have
• Logo

```html
<!DOCTYPE html>
<html lang="en">
<head>
<meta charset="utf-8">
<title>Brennick Holdings Business Cards</title>
<link rel="stylesheet" href="https://fonts.googleapis.com/css2?family=Open+Sans:wght@300;400;600&family=Playfair+Display:wght@400&display=swap">
<style>
  :root {
    --gold: #c6ad71;
    --ink: #07090b;
    --paper: #ffffff;
    --stage: #f4f4f2;
    --grey-text: #636363;
  }
  * { box-sizing: border-box; margin: 0; padding: 0; }
  html, body {
    width: 1200px; height: 1200px; overflow: hidden;
    background: var(--stage);
  }
  .canvas { position: relative; width: 1200px; height: 1200px; }
  .card {
    position: absolute; left: 290px; width: 621px; height: 373px; overflow: hidden;
  }
  .card-front { top: 194px; background: var(--paper); }
  .card-back { top: 633px; background: var(--ink); }

  .wordmark {
    position: absolute;
    font-family: "Playfair Display", Georgia, serif;
    font-weight: 400; letter-spacing: 0.02em; white-space: nowrap;
  }
  .card-front .wordmark {
    left: 38px; top: 196px; font-size: 22px; color: var(--ink);
  }
  .card-back .wordmark {
    left: 0; right: 0; top: 168px; text-align: center; font-size: 40px; color: var(--paper);
  }

  .holder { position: absolute; left: 331px; top: 78px; font-family: "Open Sans", Arial, sans-serif; }
  .holder-name { font-size: 28px; font-weight: 600; color: var(--grey-text); line-height: 1.1; letter-spacing: 0.01em; }
  .holder-title { font-size: 14px; color: var(--gold); margin-top: 2px; }
  .holder-rule { width: 53px; height: 2px; background: var(--gold); margin-top: 4px; }

  .contact-list { position: absolute; left: 332px; top: 0; list-style: none; font-family: "Open Sans", Arial, sans-serif; }
  .contact-item { position: absolute; left: 0; display: flex; align-items: center; white-space: nowrap; }
  .contact-icon {
    width: 25px; height: 25px; border-radius: 2px; background: var(--gold);
    display: flex; align-items: center; justify-content: center; flex: none;
  }
  .contact-text { margin-left: 13px; font-size: 13.5px; line-height: 1.2; color: var(--grey-text); }
  .item-address { top: 145px; }
  .item-web { top: 182px; }
  .item-mail { top: 217px; }
  .item-phone { top: 254px; }

  .footer-band { position: absolute; left: 0; bottom: 0; width: 621px; height: 44px; }

  .back-url {
    position: absolute; left: 0; right: 0; top: 305px; text-align: center;
    font-family: "Open Sans", Arial, sans-serif; font-weight: 300; font-size: 20px; color: var(--paper);
  }
</style>
</head>
<body>
<main class="canvas">
  <section class="card card-front" aria-label="Business card front">
    <div class="wordmark">BRENNICK HOLDINGS</div>

    <div class="holder">
      <h1 class="holder-name">DANIEL HARROW</h1>
      <p class="holder-title">CEO &amp; Founder</p>
      <div class="holder-rule"></div>
    </div>

    <ul class="contact-list">
      <li class="contact-item item-address">
        <span class="contact-icon">
          <svg width="12" height="15" viewBox="0 0 12 15"><path d="M6 0a5.5 5.5 0 0 0-5.5 5.5C.5 9.5 6 15 6 15s5.5-5.5 5.5-9.5A5.5 5.5 0 0 0 6 0zm0 7.6a2 2 0 1 1 0-4 2 2 0 0 1 0 4z" fill="#fff"/></svg>
        </span>
        <span class="contact-text">000 Street Name,<br>City Name, 0000 - ST</span>
      </li>
      <li class="contact-item item-web">
        <span class="contact-icon">
          <svg width="15" height="15" viewBox="0 0 16 16" fill="none" stroke="#fff" stroke-width="1.2"><circle cx="8" cy="8" r="6.5"/><ellipse cx="8" cy="8" rx="3" ry="6.5"/><path d="M1.5 8h13M2.5 4.8h11M2.5 11.2h11"/></svg>
        </span>
        <span class="contact-text">companywebsite.com</span>
      </li>
      <li class="contact-item item-mail">
        <span class="contact-icon">
          <svg width="15" height="11" viewBox="0 0 16 12" fill="none" stroke="#fff" stroke-width="1.1"><rect x="0.6" y="0.6" width="14.8" height="10.8"/><path d="M0.6 0.6L8 7l7.4-6.4M0.6 11.4l5.4-5.6M15.4 11.4L10 5.8"/></svg>
        </span>
        <span class="contact-text">youremail@company.com</span>
      </li>
      <li class="contact-item item-phone">
        <span class="contact-icon">
          <svg width="14" height="14" viewBox="0 0 24 24"><path d="M6.6 10.8a15.1 15.1 0 0 0 6.6 6.6l2.2-2.2a1 1 0 0 1 1-.25 11.4 11.4 0 0 0 3.6.57 1 1 0 0 1 1 1V20a1 1 0 0 1-1 1A17 17 0 0 1 3 4a1 1 0 0 1 1-1h3.5a1 1 0 0 1 1 1c0 1.25.2 2.45.57 3.57a1 1 0 0 1-.25 1z" fill="#fff"/></svg>
        </span>
        <span class="contact-text">+000 12345 6789</span>
      </li>
    </ul>

    <svg class="footer-band" viewBox="0 0 621 44" aria-hidden="true">
      <polygon points="0,0 684,0 709,44 0,44" transform="translate(0,0)" fill="var(--gold)"/>
      <polygon points="394,0 419,44 0,44 0,0" fill="var(--gold)"/>
      <polygon points="418,0 621,0 621,44 443,44" fill="var(--ink)"/>
    </svg>
  </section>

  <section class="card card-back" aria-label="Business card back">
    <div class="wordmark">BRENNICK HOLDINGS</div>
    <p class="back-url">companywebsite.com</p>
  </section>
</main>
</body>
</html>
```